都内でエステサロンを運営されている
美容家さんの電子書籍を出版しますので、
表紙デザイン作成をお願いいたします。

ーーーーーーーーーーー
■本のタイトル
月灯集

【サブタイトル】
朝の散歩で心を整える本

<著者>沙耶(さや)

ーーーーーーーーーー

納品は、2,560 x 1,600 ピクセルのJPEGと
元データをお願い致したく。

著者プロフィール
美容家、エステティシャン

サロンのイメージカラーはピンク、白ですが
表紙デザインに色のこだわりはありません。

ーーーー

■デザイン要望

優しさ,明るさ、清潔感と品格、プロフェッショナル感があるものをお願いします。

【コンセプト】
美容ジプシー、悩める女性たちに(男性も歓迎)贈りたい
優しく楽しい小さなご褒美タイムとその作法(洗顔やお肌のお手入れに関するメソッド)を提供する

肌質はみんなそれぞれちがいますが、本当に幸せな自分磨きは毎日のスキンケア一択。その極意を惜しみなく提供。

添付に表紙イメージの参考を挙げましたが
デザイナー様のセンスにお任せします。

ーーーーーーーーーー

※その他イラストや写真等素材を使用される場合には、商用利用可の素材をお願いします。
(Pavrelにて販売予定のため)

デザインを考えるのに必要な情報などありましたら、お答えしますので、ご遠慮なくお問い合わせ下さい。

納期は予告なく短縮する場合がございます。
よろしくお願い申し上げます。

著者様のご希望優先で決定させていただきました。

美容の道を極めた想いと、透明感、躍動感、生き生きとした理想の美人像を彷彿とさせる素敵な表紙ということで、選定させていただきます。

この度は、当コンペにご提案を頂き誠にありがとうございます。
リピートのデザイナー様もいらして、どれも素晴らしく貴重なお時間と労力を割いてくださって
本当にありがとうございました。心より感謝申し上げます。

今回選定できなかった方々の作品も大切に拝見し、個別に依頼できそうな案件などありましたらご紹介させていただきます。みなさまのご活躍祈念しております。

これからも大切に作品を制作してまいります。
どうぞまたコンペ開催の際にはご縁をいただけましたら幸いです。

本当にどうもありがとうございました。

```html
<!DOCTYPE html>
<html lang="ja">
<head>
<meta charset="utf-8">
<title>月灯集 表紙</title>
<link rel="stylesheet" href="https://fonts.googleapis.com/css2?family=Shippori+Mincho:wght@500;700&family=Noto+Sans+JP:wght@500&display=swap">
<style>
  :root {
    --pink-title: #d9667f;
    --pink-sub: #e0819a;
    --pink-wash: #f6cdd6;
    --pink-soft: #fbe6ea;
    --pink-band: #f3c9d2;
    --bubble-line: #c9d9a6;
    --ink: #2a2a2a;
    --paper: #ffffff;
  }
  * { margin: 0; padding: 0; box-sizing: border-box; }
  html, body { width: 750px; height: 1200px; overflow: hidden; background: var(--paper); }
  .cover {
    position: relative;
    width: 750px;
    height: 1200px;
    overflow: hidden;
    background: var(--paper);
    font-family: "Noto Sans JP", sans-serif;
  }
  .cover__wash {
    position: absolute;
    left: 0; top: 0;
    width: 750px; height: 570px;
    background:
      radial-gradient(ellipse 380px 240px at 120px 90px, var(--pink-wash), transparent 70%),
      radial-gradient(ellipse 420px 260px at 640px 180px, #f8d6dd, transparent 70%),
      radial-gradient(ellipse 360px 200px at 400px 470px, var(--pink-soft), transparent 75%),
      linear-gradient(180deg, #f9dde3 0%, #fcecef 70%, var(--paper) 100%);
  }
  .title-panel {
    position: absolute;
    left: 0; top: 232px;
    width: 750px; height: 196px;
    background: rgba(255, 255, 255, 0.72);
    display: flex;
    align-items: center;
    justify-content: center;
  }
  .title {
    font-family: "Shippori Mincho", serif;
    font-weight: 500;
    font-size: 116px;
    letter-spacing: 34px;
    margin-right: -34px;
    color: var(--pink-title);
    line-height: 1;
  }
  .subtitle {
    position: absolute;
    top: 578px; left: 0; width: 750px;
    display: flex;
    align-items: center;
    justify-content: center;
    gap: 12px;
    font-family: "Shippori Mincho", serif;
    font-weight: 700;
    font-size: 34px;
    color: var(--pink-sub);
    letter-spacing: 1px;
  }
  .subtitle__rule { width: 58px; height: 2px; background: var(--pink-sub); }
  .speech {
    position: absolute;
    left: 80px; top: 652px;
    width: 650px; height: 180px;
  }
  .speech__text {
    position: absolute;
    left: 0; top: 34px; width: 650px;
    text-align: center;
    font-size: 26px;
    line-height: 42px;
    color: var(--ink);
    letter-spacing: 0.5px;
  }
  .figure-art {
    position: absolute;
    left: 20px; top: 800px;
    width: 420px; height: 380px;
    background:
      radial-gradient(ellipse 120px 110px at 150px 120px, #f5c7b3, transparent 75%),
      radial-gradient(ellipse 160px 150px at 150px 280px, #f7d5cf, transparent 75%),
      radial-gradient(ellipse 110px 90px at 330px 110px, #f8d3dd, transparent 75%);
    opacity: 0.95;
  }
  .author {
    position: absolute;
    left: 498px; top: 1088px;
    display: flex;
    align-items: baseline;
    gap: 22px;
    font-family: "Shippori Mincho", serif;
    color: var(--ink);
  }
  .author__label { font-size: 28px; font-weight: 500; }
  .author__name { position: relative; font-size: 40px; font-weight: 700; letter-spacing: 16px; }
  .author__reading {
    position: absolute;
    left: 0; top: 50px; width: 100%;
    text-align: center;
    font-size: 18px;
    font-weight: 500;
    letter-spacing: 2px;
  }
  .cover__band {
    position: absolute;
    left: 0; bottom: 0;
    width: 750px; height: 30px;
    background: var(--pink-band);
  }
</style>
</head>
<body>
  <main class="cover">
    <div class="cover__wash"></div>

    <div class="title-panel">
      <h1 class="title">月灯集</h1>
    </div>

    <p class="subtitle">
      <span class="subtitle__rule"></span>
      <span>朝の散歩で心を整える本</span>
      <span class="subtitle__rule"></span>
    </p>

    <div class="speech">
      <svg width="650" height="180" viewBox="0 0 650 180" aria-hidden="true">
        <path d="M60 8 H590 Q640 8 640 72 Q640 136 590 136 H170 L118 172 L128 136 H60 Q10 136 10 72 Q10 8 60 8 Z"
              fill="var(--paper)" stroke="var(--bubble-line)" stroke-width="4" stroke-linejoin="round"/>
      </svg>
      <p class="speech__text">本当に幸せな自分磨きは毎日のスキンケア一択。<br>その極意を惜しみなく提供。</p>
    </div>

    <div class="figure-art" role="img" aria-label="花飾りを髪に挿した女性が手のひらから花びらを吹き流す水彩イラスト"></div>

    <div class="author">
      <span class="author__label">著者</span>
      <span class="author__name">沙耶<span class="author__reading">さや</span></span>
    </div>

    <div class="cover__band"></div>
  </main>
</body>
</html>
```